Web Design needed for logo design project

I am needing an interactive website for TC. Tandem Care Management is a nationwide company that combines the front desk administrative operation within Professional offices (Dental, Chiropractic, Optometry). I am needing a website designed that will provide information for potential new clients that are interested in joining our company to provide to them administrative support. I need a design for the marketing material within the folder, I will add content later. I am looking for clean crisp professional. No dancing teeth, hearts, or EKG signals please. We need it to appeal to 27-40 years old professionals. The professions are equally divided at 50/50 female to male. I already have a logo, it will be attached.
Updates

Target Market(s)

We need it to appeal to 27-40 years old professionals. The professions are equally divided at 50/50 female to male. I already have a logo, it will be attached.

Industry/Entity Type

Marketing

Requirements
Must have
• Needs to be in Word Press. It must have scalability to various screen sizes (Monitor, Phone screen, IPad, etc). Must have a customer portal capability, so professionals can access their information through a portal on the website. Have the capability to run a practice calculator or view a video requiring that it captures the visitors information so I can contact them regarding their interest in the site. Needs to have links to social media.

```html
<!DOCTYPE html>
<html lang="en">
<head>
<meta charset="utf-8">
<title>Tandem Care Management</title>
<link href="https://fonts.googleapis.com/css2?family=PT+Sans:wght@400;700&display=swap" rel="stylesheet">
<style>
:root{
  --navy:#1f4f8f;
  --sky:#42b3e5;
  --azure:#0384ce;
  --royal:#3156a3;
  --ink:#222;
  --muted:#777;
  --nav:#888;
  --page:#f7f7f7;
  --white:#fff;
}
*{margin:0;padding:0;box-sizing:border-box}
html,body{width:1200px;height:917px;overflow:hidden}
body{position:relative;background:var(--page);font-family:Arial,Helvetica,sans-serif;color:var(--ink)}
.site-header{position:absolute;left:0;top:0;width:1200px;height:142px;background:var(--white)}
.brand{position:absolute;left:128px;top:44px;display:flex;align-items:center;gap:12px;color:var(--navy);font-family:"PT Sans",sans-serif;font-weight:700;font-size:22px;line-height:1.05}
.brand-mark{width:40px;height:40px;background:var(--navy)}
.main-nav{position:absolute;left:406px;top:67px;width:630px;height:39px;font-size:13px;color:var(--nav)}
.main-nav a{text-decoration:none;color:inherit;position:absolute;top:12px;white-space:nowrap}
.main-nav .current{background:var(--sky);color:var(--white);top:0;height:39px;width:65px;display:flex;align-items:center;justify-content:center}
.hero{position:absolute;left:0;top:142px;width:1200px;height:613px;background:linear-gradient(100deg,#6aa6c9 0%,#8dbad4 40%,#d9e3e9 62%,#5b4538 80%,#2e2520 100%)}
.hero-title{position:absolute;left:131px;top:90px;font-family:"PT Sans",sans-serif;font-size:62px;line-height:66px;color:rgba(255,255,255,.6);font-weight:400}
.hero-sub{position:absolute;left:131px;top:246px;font-family:"PT Sans",sans-serif;font-size:20px;line-height:30px;color:rgba(255,255,255,.6)}
.slider-track{position:absolute;left:131px;top:382px;width:907px;height:1px;background:rgba(255,255,255,.6)}
.slider-progress{position:absolute;left:131px;top:380px;width:302px;height:5px;background:var(--white)}
.slider-label{position:absolute;top:389px;font-size:12px;color:var(--white)}
.info-box{position:absolute;top:564px;width:302px;height:191px;color:var(--white);padding:20px 28px}
.info-box h2{font-family:"PT Sans",sans-serif;font-weight:400;font-size:22px;margin-bottom:12px}
.info-box p{font-size:12.5px;line-height:17.5px}
.info-box .more{display:inline-block;margin-top:16px;border:1px solid var(--white);padding:5px 8px;font-size:12px}
.box-join{left:131px;background:var(--sky)}
.box-calculator{left:433px;background:var(--azure)}
.box-portal{left:735px;background:var(--royal)}
.portal-row{display:flex;justify-content:space-between;align-items:center;font-size:12.5px;border-bottom:1px solid rgba(255,255,255,.3);padding:8px 0 11px}
.social{display:flex;gap:6px}
.social span{width:14px;height:14px;border-radius:50%;background:var(--white)}
.section-title{position:absolute;top:782px;font-family:"PT Sans",sans-serif;font-size:16px;font-weight:400}
.section-title::after{content:"";position:absolute;left:0;top:27px;width:40px;height:2px;background:var(--sky)}
.post-date{position:absolute;top:838px;height:33px;display:flex;gap:4px;font-size:12.5px;color:var(--white)}
.post-date span{display:flex;align-items:center;padding:0 11px;background:var(--royal)}
.post-date .count{background:var(--sky);padding:0 9px}
.post-photo{position:absolute;left:131px;top:896px;width:275px;height:21px;background:linear-gradient(90deg,#d8cfc4,#bfa98f)}
.post-title{position:absolute;left:433px;top:892px;font-family:"PT Sans",sans-serif;font-size:22px;font-weight:400;white-space:nowrap}
.dept-head{position:absolute;left:735px;top:838px;width:303px;height:34px;background:var(--royal);color:var(--white);font-family:"PT Sans",sans-serif;font-size:16px;padding:8px 11px;display:flex;justify-content:space-between}
.dept-photo{position:absolute;left:735px;top:893px;width:69px;height:24px;background:linear-gradient(90deg,#9aa7a4,#d5dcd9)}
.dept-text{position:absolute;left:822px;top:893px;width:216px;font-size:12px;line-height:17px;color:var(--muted)}
</style>
</head>
<body>
<header class="site-header">
  <div class="brand"><span class="brand-mark"></span><span>Tandem Care<br>Management</span></div>
  <nav class="main-nav">
    <a class="current" style="left:0">HOME</a>
    <a style="left:94px">ABOUT</a>
    <a style="left:166px">SERVICES</a>
    <a style="left:257px">CALCULATOR</a>
    <a style="left:372px">VIDEO</a>
    <a style="left:442px">PORTAL</a>
    <a style="left:522px">CONTACT</a>
  </nav>
</header>

<section class="hero" role="img" aria-label="Photo of a smiling professional stretching her arms against a blue sky">
  <h1 class="hero-title">Front desk,<br>handled</h1>
  <p class="hero-sub">Administrative support for dental,<br>chiropractic and optometry offices</p>
  <div class="slider-track"></div>
  <div class="slider-progress"></div>
  <span class="slider-label" style="left:131px">1</span>
  <span class="slider-label" style="left:432px">2</span>
</section>

<div class="info-box box-join">
  <h2>Join Our Network</h2>
  <p>Tandem Care runs the front desk of professional offices nationwide, so your team can focus fully on patients.</p>
  <span class="more">Read more &rarr;</span>
</div>
<div class="info-box box-calculator">
  <h2>Practice Calculator</h2>
  <p>See what shared administration could save your office. Leave your details to run the calculator or watch our video.</p>
  <span class="more">Try it now &rarr;</span>
</div>
<div class="info-box box-portal">
  <h2>Client Portal</h2>
  <div class="portal-row"><span>Practice reports</span><span>Sign in</span></div>
  <div class="portal-row"><span>Billing summary</span><span>Sign in</span></div>
  <div class="portal-row"><span>Follow us</span><span class="social" aria-label="Social media links"><span></span><span></span><span></span><span></span></span></div>
</div>

<h3 class="section-title" style="left:131px">Latest News</h3>
<h3 class="section-title" style="left:735px">Specialties</h3>

<div class="post-date" style="left:131px"><span>12 DEC 12</span><span class="count">2</span></div>
<div class="post-date" style="left:433px"><span>12 DEC 12</span><span class="count">3</span></div>
<div class="post-photo" role="img" aria-label="News photo of a front desk team at work"></div>
<h4 class="post-title">Why offices share a front desk</h4>

<div class="dept-head"><span>Dental Offices</span><span>&minus;</span></div>
<div class="dept-photo" role="img" aria-label="Photo of a dental office reception"></div>
<p class="dept-text">Scheduling, billing and patient intake handled by our trained remote team.</p>
</body>
</html>
```